Business Card and Letterhead for Pemlo - modern real estate business

I need a double sided business card design for Pemlo. Please see business card brief here https://files.quillnote-hub.net/page/7RtxQmZbn4LsWe2VyHoPk9dFjuC3gaXrTmqEi5Ns_pz/view?mode=shared

Please feel free to design the business cards however you feel best. I am happy to give some creative freedoms and then provide feedback from there.

Please then also create a letterhead to match the business card design

Colors

Designer to choose colors to be used in the design.

Requirements
Must have
• Must be a modern, elegant business card which looks very professional

```html
<!DOCTYPE html>
<html lang="en">
<head>
<meta charset="utf-8">
<title>Pemlo Letterhead</title>
<link rel="stylesheet" href="https://fonts.googleapis.com/css2?family=Montserrat:wght@400;500;700&family=Open+Sans:wght@400&display=swap">
<style>
  :root {
    --backdrop: #a5b7bd;
    --paper: #ffffff;
    --brand-red: #e1141d;
    --ink: #1c1c1c;
    --body-ink: #3d3d3d;
    --base-bar: #262626;
    --signature-tone: #eceef0;
  }
  * { margin: 0; padding: 0; box-sizing: border-box; }
  html, body {
    width: 1200px; height: 900px; overflow: hidden;
    background: var(--backdrop);
  }
  .letterhead {
    position: absolute; left: 293px; top: 57px;
    width: 614px; height: 785px;
    background: var(--paper);
    box-shadow: 0 2px 6px rgba(0,0,0,0.18);
  }
  .letterhead__base-bar {
    position: absolute; left: 0; right: 0; bottom: 0; height: 6px;
    background: var(--base-bar);
  }
  .brand-name {
    position: absolute; left: 38px; top: 38px;
    font-family: "Montserrat", sans-serif; font-weight: 700;
    font-size: 35px; letter-spacing: 0.5px; line-height: 1;
    color: var(--brand-red);
  }
  .company-details {
    position: absolute; left: 474px; top: 27px;
    font-family: "Montserrat", sans-serif; font-weight: 500;
    font-size: 10px; line-height: 12.5px; color: var(--ink);
  }
  .company-details .registration { margin-top: 2px; }
  .letter {
    position: absolute; left: 68px; top: 219px; width: 480px;
    font-family: "Open Sans", sans-serif; font-size: 10px;
    color: var(--body-ink);
  }
  .letter__date { height: 50px; line-height: 14px; }
  .letter__para { line-height: 22px; white-space: nowrap; }
  .letter__para + .letter__para { margin-top: 2px; }
  .letter__para--spaced { margin-top: 4px !important; }
  .sign-off {
    position: absolute; left: 422px; top: 553px;
    font-family: "Open Sans", sans-serif; font-size: 10px;
    line-height: 12px; color: var(--body-ink);
  }
  .sign-off__signature {
    width: 125px; height: 38px; margin-left: -6px; margin-bottom: 4px;
    background: linear-gradient(90deg, var(--signature-tone), #f7f8f9);
    border-radius: 3px;
  }
  .contact-bar {
    position: absolute; left: 0; right: 0; top: 758px;
    display: flex; justify-content: center; gap: 14px;
    font-family: "Montserrat", sans-serif; font-size: 10px;
    color: var(--ink);
  }
  .contact-bar__item { display: flex; align-items: center; gap: 4px; }
  .contact-bar__icon { width: 9px; height: 9px; }
</style>
</head>
<body>
<main class="letterhead">
  <div class="brand-name">PEMLO</div>

  <address class="company-details" style="font-style:normal">
    <div>PO Box 7316</div>
    <div>Larkvale NSW 2690</div>
    <div class="registration">ABN: 41 208 915 336</div>
    <div>Lic No. 20478163</div>
  </address>

  <article class="letter">
    <p class="letter__date">Date, 10 September, 2020</p>
    <p class="letter__para">This is a sample letter that has been placed to demonstrate typing remat (Your Company). letterhead<br>design. When positioned properly, it will serve to work in harmony with all other elements letterhead.<br>This letterhead design is meant to project an image</p>
    <p class="letter__para">This letterhead design is meant project an image of professionalism reliability. By using simple aligen<br>we have created a very spacious feeling. The simplicity suggest&nbsp; rengththe spaciousnes contributes h<br>aesthetics the layout. These basic qualities along with the (Your Company)</p>
    <p class="letter__para letter__para--spaced">look and helps reinforce the (Your Company) brand. letterhead design is meant to project an image p<br>design. When positioned properly, it will serve to work in harmony all the other elements letterhead.<br>sionalism and reliability.</p>
    <p class="letter__para letter__para--spaced">This letterhead design is based on the (Form of your logo) form (Your Company) logo. Each stationery<br>we have created a very spacious feeling. The simplicity suggests strength the spaciousnes contribute<br>part of the (Form of your logo).</p>
  </article>

  <div class="sign-off">
    <div class="sign-off__signature" role="img" aria-label="Handwritten signature of Daniel Harlow"></div>
    <div>Daniel Harlow</div>
    <div>Manager</div>
  </div>

  <footer class="contact-bar">
    <span class="contact-bar__item">
      <svg class="contact-bar__icon" viewBox="0 0 10 10"><circle cx="5" cy="5" r="5" fill="var(--brand-red)"/><path d="M3.2 2.6l1 1-.5.7c.4.8 1 1.4 1.8 1.8l.7-.5 1 1-.6.9C4.6 7.2 2.8 5.4 2.3 3.2z" fill="#fff"/></svg>
      02 5186 3947
    </span>
    <span class="contact-bar__item">
      <svg class="contact-bar__icon" viewBox="0 0 10 10"><circle cx="5" cy="5" r="5" fill="var(--brand-red)"/><rect x="2.6" y="3.3" width="4.8" height="3.4" fill="#fff"/><path d="M2.6 3.3L5 5.2l2.4-1.9" fill="none" stroke="var(--brand-red)" stroke-width="0.6"/></svg>
      info@pemlo.com
    </span>
    <span class="contact-bar__item">
      <svg class="contact-bar__icon" viewBox="0 0 10 10"><circle cx="5" cy="5" r="5" fill="var(--brand-red)"/><circle cx="5" cy="5" r="2.4" fill="none" stroke="#fff" stroke-width="0.8"/><path d="M2.6 5h4.8" stroke="#fff" stroke-width="0.6"/></svg>
      www.pemlo.com
    </span>
  </footer>

  <div class="letterhead__base-bar"></div>
</main>
</body>
</html>
```